Marist District College Brenthollow Letterhead

Our college is called Marist District College Brenthollow. We would like to request a few letterhead design options to choose from please. We look forward to seeing some new and fresh ideas for our College Letterhead.

Please note that the College has the following PMS Colours:
MAROON – PMS 229C
BLUE – PMS 2747C
GOLD – PMS 871C
YELLOW – PMS 123C

Our College Motto is:
Light guiding Purpose.
I have attached a copy of our current letterhead and College Logo.

Please note that the letterhead must include the following details:

Marist District College Brenthollow
Light Guiding Purpose
Phone: 9472 0000
Fax:9481 3157
Address: 517 Brenthollow Road Brenthollow 3037
Mail:PO BOX 4817 Wattle Bend VIC 3038 Australia
ABN 47 816 205 938

www.mdcbrenthollow-example.net
https://twitter.com/mdcbrenthollow
https://www.pinterest.com/mdcbrenthollow
https://www.facebook.com/MDCBrenthollow
www.videohub-example.com (search MDC Brenthollow)

Please feel free to contact me on the below detail if I can further assist.

Regards,
Joanna Verkuil
reception@mdcbrenthollow-example.net
PH: 9472 0000

Target Market(s)

College Community

Industry/Entity Type

Education

Requirements
Must have
• See Project Description
Nice to have
• see Project Description

```html
<!DOCTYPE html>
<html lang="en">
<head>
<meta charset="utf-8">
<title>Marist District College Brenthollow — Letterhead</title>
<link href="https://fonts.googleapis.com/css2?family=Roboto+Condensed:wght@400;700&family=Exo+2:ital,wght@1,600&display=swap" rel="stylesheet">
<style>
  :root {
    --navy: #172a55;
    --gold: #8a6d4a;
    --yellow: #ffd200;
    --maroon: #8a1f2f;
    --paper: #ffffff;
    --backdrop: #e9e9e9;
    --ink: #1d1d1d;
  }
  * { box-sizing: border-box; margin: 0; padding: 0; }
  html, body { width: 1200px; height: 1200px; overflow: hidden; }
  body {
    background: var(--backdrop);
    font-family: "Roboto Condensed", "Arial Narrow", sans-serif;
    position: relative;
  }
  .letterhead {
    position: absolute;
    left: 204px; top: 40px;
    width: 791px; height: 1120px;
    background: var(--paper);
    overflow: hidden;
  }
  .header-wave { position: absolute; left: 0; top: 0; width: 791px; height: 210px; }
  .college-mark {
    position: absolute; left: 60px; top: 72px;
    display: flex; align-items: center; gap: 12px;
  }
  .college-mark__dot { width: 40px; height: 40px; border-radius: 50%; background: var(--maroon); flex: none; }
  .college-mark__name {
    color: var(--navy); font-weight: 700; font-size: 19px; line-height: 1.15; width: 150px;
  }
  .college-title {
    position: absolute; left: 541px; top: 28px; transform: translateX(-50%);
    color: var(--yellow); font-size: 25px; font-weight: 400; white-space: nowrap; letter-spacing: -0.2px;
  }
  .contact { position: absolute; color: #fff; font-size: 11px; line-height: 13px; white-space: nowrap; }
  .contact--web { right: 243px; top: 90px; display: flex; align-items: center; gap: 6px; }
  .contact--abn { right: 243px; top: 110px; }
  .contact-divider { position: absolute; left: 558px; top: 69px; width: 1.5px; height: 91px; background: var(--yellow); }
  .contact-row { position: absolute; left: 566px; display: flex; align-items: flex-start; gap: 9px; }
  .icon { width: 14px; height: 12px; flex: none; }
  .footer-links {
    position: absolute; left: 0; right: 0; top: 1063px;
    display: flex; justify-content: center; gap: 14px;
    font-size: 10px; color: var(--ink); white-space: nowrap;
  }
  .footer-links__item { display: flex; align-items: center; gap: 5px; }
  .footer-links__item::before { content: ""; width: 10px; height: 10px; background: var(--navy); }
  .footer-band {
    position: absolute; left: 0; bottom: 0; width: 100%; height: 37px;
    background: var(--navy);
    display: flex; align-items: center; justify-content: center;
  }
  .motto {
    font-family: "Exo 2", sans-serif; font-style: italic; font-weight: 600;
    color: var(--yellow); font-size: 15px; letter-spacing: 0.6px; text-transform: uppercase;
  }
</style>
</head>
<body>
  <main class="letterhead">
    <svg class="header-wave" viewBox="0 0 791 210" aria-hidden="true">
      <path d="M232,0 C380,160 555,206 660,199 C725,195 762,184 791,173 L791,0 Z" fill="var(--gold)"/>
      <path d="M251,0 C400,150 560,196 660,194 C720,192 760,180 791,169 L791,0 Z" fill="var(--navy)"/>
    </svg>

    <div class="college-mark">
      <span class="college-mark__dot"></span>
      <span class="college-mark__name">Marist District College Brenthollow</span>
    </div>

    <h1 class="college-title">Marist District College Brenthollow</h1>

    <div class="contact contact--web">
      <svg class="icon" viewBox="0 0 14 12"><rect width="14" height="12" fill="var(--yellow)"/><circle cx="7" cy="6" r="4" fill="none" stroke="var(--navy)" stroke-width="1.2"/><path d="M3,6H11M7,2V10" stroke="var(--navy)" stroke-width="1"/></svg>
      <span>www.mdcbrenthollow-example.net</span>
    </div>
    <div class="contact contact--abn">ABN 47 816 205 938</div>

    <div class="contact-divider"></div>

    <div class="contact contact-row" style="top:65px">
      <svg class="icon" viewBox="0 0 14 12"><path d="M1,5 Q7,0 13,5 L11,6 L9,4 H5 L3,6 Z M3,7 H11 V11 H3 Z" fill="var(--yellow)"/></svg>
      <span>9472 0000</span>
    </div>
    <div class="contact contact-row" style="top:84px">
      <svg class="icon" viewBox="0 0 14 12"><rect x="1" y="4" width="12" height="8" fill="var(--yellow)"/><rect x="3" y="0" width="8" height="5" fill="var(--yellow)" stroke="var(--navy)" stroke-width="0.8"/><rect x="3" y="7" width="8" height="2" fill="var(--navy)"/></svg>
      <span>9481 3157</span>
    </div>
    <div class="contact contact-row" style="top:103px">
      <span class="icon"></span>
      <span>517 Brenthollow Road<br>Brenthollow 3094</span>
    </div>
    <div class="contact contact-row" style="top:135px">
      <svg class="icon" viewBox="0 0 14 12"><rect x="0.5" y="1" width="13" height="10" fill="var(--yellow)"/><path d="M2,3 L7,7 L12,3" fill="none" stroke="var(--navy)" stroke-width="1.2"/></svg>
      <span>PO BOX 4817 Wattle Bend<br>VIC 3095 Australia</span>
    </div>

    <div class="footer-links">
      <span class="footer-links__item">chirpnet-example.com/mdcbrenthollow</span>
      <span class="footer-links__item">pinboard-example.com/mdcbrenthollow</span>
      <span class="footer-links__item">friendsnet-example.com/MDCBrenthollow</span>
      <span class="footer-links__item">videohub-example.com (search MDC Brenthollow)</span>
    </div>

    <footer class="footer-band">
      <p class="motto">Light Guiding Purpose</p>
    </footer>
  </main>
</body>
</html>
```